Creative & Appealing Business Card

Required a business card for Ferndale Recoveries
We specialise in claims management services for PPI ( Payment Protection Insurance.
2 sided business card
Round Corners
I like embossed and raised lettering

Industry/Entity Type

Business

```html
<!DOCTYPE html>
<html lang="en">
<head>
<meta charset="utf-8">
<title>Ferndale Recoveries – Business Card</title>
<link href="https://fonts.googleapis.com/css2?family=Open+Sans:wght@400;600;700&display=swap" rel="stylesheet">
<style>
  :root {
    --bg: #cfcfcf;
    --card: #050505;
    --band: #161616;
    --ink: #ffffff;
    --ink-soft: #e6e6e6;
  }
  * { box-sizing: border-box; margin: 0; padding: 0; }
  html, body { width: 1200px; height: 900px; overflow: hidden; }
  body {
    background: var(--bg);
    font-family: "Open Sans", Arial, sans-serif;
    color: var(--ink);
    display: flex;
    flex-direction: column;
    align-items: center;
    justify-content: center;
    gap: 36px;
  }
  .card {
    position: relative;
    width: 700px;
    height: 400px;
    background: var(--card);
    border-radius: 18px;
    overflow: hidden;
  }

  /* brand lockup */
  .brand { display: flex; align-items: center; gap: 18px; }
  .brand-dot {
    width: 74px; height: 74px; border-radius: 50%;
    background: var(--ink); flex: none;
  }
  .brand-name {
    font-weight: 700; font-size: 36px; line-height: 1.02;
    letter-spacing: 0.5px; text-transform: uppercase; color: var(--ink);
  }

  /* front side */
  .card-front .brand { position: absolute; left: 50%; top: 62px; transform: translateX(-50%); }
  .tagline {
    position: absolute; left: 0; right: 0; top: 200px;
    text-align: center; font-weight: 700; font-size: 17px;
  }
  .card-front .rule { position: absolute; left: 0; right: 0; top: 238px; height: 6px; background: var(--ink); }
  .services {
    position: absolute; left: 0; right: 0; top: 262px;
    text-align: center; font-size: 19px; line-height: 1.35; color: var(--ink-soft);
  }

  /* back side */
  .card-back .brand { position: absolute; left: 44px; top: 48px; }
  .holder-name {
    position: absolute; right: 48px; top: 62px;
    font-weight: 600; font-size: 24px; letter-spacing: 1.5px; text-transform: uppercase;
  }
  .contact-band {
    position: absolute; left: 0; right: 0; top: 196px; height: 150px;
    background: var(--band);
  }
  .card-back .rule { position: absolute; left: 0; right: 0; top: 346px; height: 6px; background: var(--ink); }
  .contact-list {
    position: absolute; left: 40px; right: 32px; top: 222px;
    display: flex; justify-content: space-between; font-size: 15.5px; line-height: 1.6;
    color: var(--ink-soft);
  }
  .contact-group { display: flex; flex-direction: column; gap: 6px; }
  .contact-group.phones { padding-top: 34px; }
  .contact-group.online { padding-top: 58px; }
  .contact-item { display: flex; align-items: flex-start; gap: 10px; }
  .contact-item svg { width: 15px; height: 15px; margin-top: 4px; flex: none; fill: var(--ink); }
</style>
</head>
<body>

  <section class="card card-front" aria-label="Card front">
    <div class="brand">
      <span class="brand-dot"></span>
      <span class="brand-name">Ferndale<br>Recoveries</span>
    </div>
    <p class="tagline">Claims Management Service for mis-sold</p>
    <div class="rule"></div>
    <p class="services">Payment Protection Insurance Claims<br>Interest Rate Hedging Products / SWAPS</p>
  </section>

  <section class="card card-back" aria-label="Card back">
    <div class="brand">
      <span class="brand-dot"></span>
      <span class="brand-name">Ferndale<br>Recoveries</span>
    </div>
    <p class="holder-name">Daniel Marsh</p>
    <div class="contact-band"></div>
    <div class="rule"></div>

    <div class="contact-list">
      <div class="contact-group address">
        <div class="contact-item">
          <svg viewBox="0 0 16 16" aria-hidden="true"><path d="M8 0a5.5 5.5 0 0 0-5.5 5.5C2.5 9.6 8 16 8 16s5.5-6.4 5.5-10.5A5.5 5.5 0 0 0 8 0zm0 8a2.5 2.5 0 1 1 0-5 2.5 2.5 0 0 1 0 5z"/></svg>
          <span>48 Linden Grove<br>London, W2 5QT</span>
        </div>
      </div>
      <div class="contact-group phones">
        <div class="contact-item">
          <svg viewBox="0 0 16 16" aria-hidden="true"><path d="M3.5 1l2.5 3-1.5 2c1 2 3 4 5 5l2-1.5 3 2.5-1.5 2.5C8 15 1 8 1 2.5z"/></svg>
          <span>44 (0) 333 000 0147</span>
        </div>
        <div class="contact-item">
          <svg viewBox="0 0 16 16" aria-hidden="true"><rect x="2" y="5" width="12" height="10" rx="1.5"/><rect x="4" y="1" width="8" height="3" rx="1"/></svg>
          <span>44 (0) 203 000 0582</span>
        </div>
      </div>
      <div class="contact-group online">
        <div class="contact-item">
          <svg viewBox="0 0 16 16" aria-hidden="true"><path d="M1 3h14v10H1z M1 3l7 6 7-6" stroke="#161616" stroke-width="1.2"/></svg>
          <span>daniel@ferndalerecoveries.com</span>
        </div>
        <div class="contact-item">
          <svg viewBox="0 0 16 16" aria-hidden="true"><path d="M6.5 9.5l3-3M5 7.5L3 9.5a2.5 2.5 0 0 0 3.5 3.5l2-2M11 8.5l2-2A2.5 2.5 0 0 0 9.5 3l-2 2" fill="none" stroke="#fff" stroke-width="1.8" stroke-linecap="round"/></svg>
          <span>www.ferndalerecoveries.com</span>
        </div>
      </div>
    </div>
  </section>

</body>
</html>
```